Create Vertical Dog Food Labels (3 inches x 5 inches) for PupKitchen

We need a packing Vertical label (3 inches x 5 inches) design for our line of Dog Food - Pup Kitchen at pupkitchenmeals.com (please review website). This design is for Custom Roll Labels. We have a logo already. Use our logo colors on label. What we need incorporated is a list of our ingredients:

50% Choice Beef
20% Pasture-raised Chicken
15% Brown Rice
15% Fresh Vegetables - Carrots, Kale, Zucchini
Herbal Health Boosters

We also need these lines at the bottom of the label:

Keeps in fridge for 4 days after thawing
Stores in freezer up to 6 months
Questions? email us at orders@meadowlanepantry.com

We have attached a sample of a competitor. The Kibble Crate.

Target Market(s)

Dog owners

Industry/Entity Type

Dog Food

Font styles to use
Sans Serif

Requirements
Must have
• Read project description above
Nice to have
• Our logo color incorporated
Should not have
• I want it simple.

```html
<!DOCTYPE html>
<html lang="en">
<head>
<meta charset="utf-8">
<title>PupKitchen Dog Food Labels</title>
<link rel="stylesheet" href="https://fonts.googleapis.com/css2?family=Bebas+Neue&family=Poppins:wght@400;600;700&display=swap">
<style>
  :root {
    --stage-bg: #cccccc;
    --label-green: #a8e36a;
    --label-orange: #f5bd45;
    --brand-green: #1f6e1c;
    --accent-orange: #f2683a;
    --ink: #111111;
    --white: #ffffff;
    --art-tone: rgba(0, 0, 0, 0.14);
  }
  * { margin: 0; padding: 0; box-sizing: border-box; }
  html, body { width: 1200px; height: 940px; overflow: hidden; }
  body { background: var(--stage-bg); position: relative; }

  .label {
    position: absolute;
    top: 78px;
    width: 470px;
    height: 783px;
    color: var(--ink);
  }
  .label--green { left: 92px; background: var(--label-green); --storage-ink: var(--brand-green); --contact-ink: var(--brand-green); }
  .label--orange { left: 637px; background: var(--label-orange); --storage-ink: var(--accent-orange); --contact-ink: var(--ink); }

  .brand-tab {
    position: absolute;
    left: 77px; top: 0;
    width: 306px; height: 233px;
    background: var(--white);
    border-radius: 0 0 14px 14px;
  }
  .brand-dot {
    position: absolute;
    left: 93px; top: 38px;
    width: 120px; height: 120px;
    border-radius: 50%;
    background: var(--brand-green);
  }
  .brand-name {
    position: absolute;
    left: 0; top: 160px;
    width: 100%;
    text-align: center;
    font: 600 42px/46px "Poppins", sans-serif;
    color: var(--brand-green);
  }

  .product-title {
    position: absolute;
    left: 0; top: 264px;
    width: 100%;
    text-align: center;
    font: 700 60px/64px "Poppins", sans-serif;
    letter-spacing: -0.5px;
  }
  .product-subtitle {
    position: absolute;
    left: 0; top: 331px;
    width: 100%;
    text-align: center;
    font: 400 32px/36px "Poppins", sans-serif;
    letter-spacing: 1px;
  }
  .rule {
    position: absolute;
    top: 342px;
    width: 28px; height: 4px;
    background: var(--ink);
    border-radius: 2px;
  }
  .rule--left { left: 62px; }
  .rule--right { left: 380px; }

  .ingredient-art {
    position: absolute;
    background: var(--art-tone);
    border-radius: 10px;
  }
  .art-beef { left: 68px; top: 390px; width: 57px; height: 66px; }
  .art-rice { left: 189px; top: 402px; width: 68px; height: 46px; }
  .art-chicken { left: 326px; top: 390px; width: 74px; height: 66px; }
  .art-greens { left: 112px; top: 508px; width: 66px; height: 50px; }
  .art-vegetables { left: 255px; top: 497px; width: 85px; height: 61px; }

  .ingredient-name {
    position: absolute;
    width: 200px;
    text-align: center;
    font: 400 17px/16px "Bebas Neue", sans-serif;
    letter-spacing: 0.3px;
  }
  .name-beef { left: -3px; top: 462px; }
  .name-rice { left: 124px; top: 462px; }
  .name-chicken { left: 263px; top: 462px; }
  .name-greens { left: 45px; top: 563px; }
  .name-vegetables { left: 198px; top: 563px; }

  .storage-note {
    position: absolute;
    left: 36px; top: 623px;
    width: 399px; height: 65px;
    background: var(--white);
    border-radius: 10px;
    padding-top: 7px;
    text-align: center;
    font: 400 24px/29px "Bebas Neue", sans-serif;
    color: var(--storage-ink);
    letter-spacing: 0.3px;
  }

  .contact {
    position: absolute;
    left: 0; top: 721px;
    width: 100%;
    text-align: center;
    font: 400 21px/22px "Bebas Neue", sans-serif;
    color: var(--contact-ink);
    letter-spacing: 0.3px;
  }
</style>
</head>
<body>

<section class="label label--green">
  <div class="brand-tab">
    <span class="brand-dot"></span>
    <div class="brand-name">PupKitchen</div>
  </div>
  <h1 class="product-title">DOG FOOD</h1>
  <span class="rule rule--left"></span>
  <p class="product-subtitle">PUP KITCHEN</p>
  <span class="rule rule--right"></span>

  <div class="ingredient-art art-beef" role="img" aria-label="Line drawing of a beef steak"></div>
  <div class="ingredient-art art-rice" role="img" aria-label="Line drawing of rice grains"></div>
  <div class="ingredient-art art-chicken" role="img" aria-label="Line drawing of a whole chicken"></div>
  <div class="ingredient-art art-greens" role="img" aria-label="Line drawing of leafy herbs"></div>
  <div class="ingredient-art art-vegetables" role="img" aria-label="Line drawing of carrots, kale and zucchini"></div>

  <p class="ingredient-name name-beef">50% Choice Beef</p>
  <p class="ingredient-name name-rice">15% Brown Rice</p>
  <p class="ingredient-name name-chicken">20% Pasture-Raised<br>Chicken</p>
  <p class="ingredient-name name-greens">Herbal Health<br>Boosters</p>
  <p class="ingredient-name name-vegetables">15% Fresh Vegetables<br>Carrots, Kale, Zucchini</p>

  <p class="storage-note">Keeps in fridge for 4 days after thawing<br>Stores in freezer up to 6 months</p>
  <p class="contact">Questions? Email us at<br>orders@meadowlanepantry.com</p>
</section>

<section class="label label--orange">
  <div class="brand-tab">
    <span class="brand-dot"></span>
    <div class="brand-name">PupKitchen</div>
  </div>
  <h1 class="product-title">DOG FOOD</h1>
  <span class="rule rule--left"></span>
  <p class="product-subtitle">PUP KITCHEN</p>
  <span class="rule rule--right"></span>

  <div class="ingredient-art art-beef" role="img" aria-label="Line drawing of a beef steak"></div>
  <div class="ingredient-art art-rice" role="img" aria-label="Line drawing of rice grains"></div>
  <div class="ingredient-art art-chicken" role="img" aria-label="Line drawing of a whole chicken"></div>
  <div class="ingredient-art art-greens" role="img" aria-label="Line drawing of leafy herbs"></div>
  <div class="ingredient-art art-vegetables" role="img" aria-label="Line drawing of carrots, kale and zucchini"></div>

  <p class="ingredient-name name-beef">50% Choice Beef</p>
  <p class="ingredient-name name-rice">15% Brown Rice</p>
  <p class="ingredient-name name-chicken">20% Pasture-Raised<br>Chicken</p>
  <p class="ingredient-name name-greens">Herbal Health<br>Boosters</p>
  <p class="ingredient-name name-vegetables">15% Fresh Vegetables<br>Carrots, Kale, Zucchini</p>

  <p class="storage-note">Keeps in fridge for 4 days after thawing<br>Stores in freezer up to 6 months</p>
  <p class="contact">Questions? Email us at<br>orders@meadowlanepantry.com</p>
</section>

</body>
</html>
```